I Need a Banner for Web Advertising

impression banner for zentora AD
size 728x90, 320x50 , 160x600 , 300x600 , 100x50
Banner background bright blue
would like the AD to say -
We pay cash for houses in any condition
Probate,foreclosure, Pass due property taxes ect
470-555-0193
Updates
We would like to change the words to -
We pay cash for houses in any condition!
Probate, Foreclosure, Pass Due Property Taxes, and more!
470-555-0193
Target Market(s)
consumers that need to sale
Industry/Entity Type
Real Estate

```html
<!DOCTYPE html>
<html lang="en">
<head>
<meta charset="utf-8">
<title>Zentora web banner set</title>
<link rel="stylesheet" href="https://fonts.googleapis.com/css2?family=Montserrat:wght@800;900&family=Open+Sans:wght@400;600&family=Exo+2:wght@600&display=swap">
<style>
:root{
  --ink:#111111;
  --frame:#2a2a2a;
  --paper:#ffffff;
  --blue-top:#0890cc;
  --blue-bottom:#0b6596;
  --orange-top:#e88d1f;
  --orange-bottom:#b86d1a;
  --call:#ea8a1c;
}
*{margin:0;padding:0;box-sizing:border-box}
html,body{width:1200px;height:647px;overflow:hidden;background:var(--paper)}
.canvas{position:relative;width:1200px;height:647px}
.banner{position:absolute;background:var(--paper);border:2px solid var(--frame);overflow:hidden}
.banner svg.shapes{position:absolute;inset:0;width:100%;height:100%}
.banner .layer{position:absolute;text-align:center}
.brand{font-family:"Montserrat",sans-serif;font-weight:900;color:var(--ink);letter-spacing:-0.5px;line-height:1}
.call{font-family:"Exo 2",sans-serif;font-weight:600;color:var(--ink);line-height:1}
.call .label{color:var(--call)}
.headline{font-family:"Montserrat",sans-serif;font-weight:800;color:var(--paper);line-height:1.15}
.services{font-family:"Open Sans",sans-serif;font-weight:400;color:var(--paper);line-height:1.25}

/* 300x600 */
.tower-wide{left:57px;top:82px;width:254px;height:508px}
.tower-wide .brand{left:0;right:0;top:38px;font-size:34px}
.tower-wide .call{left:0;right:0;top:92px;font-size:29px}
.tower-wide .call .label{display:block;font-size:27px;margin-bottom:4px}
.tower-wide .headline{left:0;right:0;top:187px;font-size:31px;line-height:1.16}
.tower-wide .services{left:0;right:0;top:412px;font-size:19.5px}

/* 160x600 */
.tower-narrow{left:345px;top:82px;width:135px;height:508px}
.tower-narrow .brand{left:0;right:0;top:28px;font-size:21px;line-height:1.15}
.tower-narrow .call{left:0;right:0;top:112px;font-size:18px}
.tower-narrow .call .label{display:block;margin-bottom:4px}
.tower-narrow .headline{left:0;right:0;top:212px;font-size:19px;line-height:1.2}
.tower-narrow .services{left:0;right:0;top:386px;font-size:14px;line-height:1.5}

/* 728x90 */
.leader{left:516px;top:111px;width:657px;height:81px}
.leader .brand{left:0;width:240px;top:16px;font-size:30px}
.leader .call{left:0;width:240px;top:56px;font-size:15px}
.leader .headline{left:245px;width:210px;top:6px;font-size:19.5px;line-height:1.1}
.leader .services{left:462px;width:195px;top:15px;font-size:14.5px;line-height:1.05}

/* 320x50 */
.mobile{left:516px;top:231px;width:490px;height:76px;border-color:#6b6b6b}
.mobile .brand{left:0;width:178px;top:17px;font-size:22px}
.mobile .call{left:0;width:178px;top:48px;font-size:11px}
.mobile .headline{left:180px;width:168px;top:12px;font-size:15px;line-height:1.1}
.mobile .services{left:350px;width:138px;top:17px;font-size:10.5px;line-height:1.25;font-weight:600}

/* 100x50 */
.tile{left:516px;top:336px;width:107px;height:54px;border-width:1px;border-color:#555}
.tile .brand{left:0;right:0;top:4px;font-size:11px}
.tile .call{left:0;right:0;top:19px;font-size:5.5px}
.tile .headline{left:1px;width:51px;top:30px;font-size:4.2px;line-height:1.2}
.tile .services{left:53px;width:52px;top:30px;font-size:4.2px;line-height:1.2;font-weight:600}
</style>
</head>
<body>
<main class="canvas">

  <section class="banner tower-wide" aria-label="300 by 600 banner">
    <svg class="shapes" viewBox="0 0 254 508" preserveAspectRatio="none" aria-hidden="true">
      <defs>
        <linearGradient id="blueA" x1="0" y1="0" x2="0" y2="1"><stop offset="0" stop-color="var(--blue-top)"/><stop offset="1" stop-color="var(--blue-bottom)"/></linearGradient>
        <linearGradient id="orangeA" x1="0" y1="0" x2="0" y2="1"><stop offset="0" stop-color="var(--orange-top)"/><stop offset="1" stop-color="var(--orange-bottom)"/></linearGradient>
      </defs>
      <path d="M0,167 Q110,140 254,196 L254,378 Q120,420 0,365 Z" fill="url(#blueA)"/>
      <path d="M0,368 Q120,425 254,388 L254,508 L0,508 Z" fill="url(#orangeA)"/>
    </svg>
    <div class="layer brand">ZENTORA</div>
    <div class="layer call"><span class="label">CALL:</span>470-555-0193</div>
    <div class="layer headline">WE PAY<br>CASH FOR<br>HOUSES<br>IN ANY<br>CONDITION!</div>
    <div class="layer services">Probate, Foreclosure,<br>Pass Due Property<br>Taxes, and more!</div>
  </section>

  <section class="banner tower-narrow" aria-label="160 by 600 banner">
    <svg class="shapes" viewBox="0 0 135 508" preserveAspectRatio="none" aria-hidden="true">
      <defs>
        <linearGradient id="blueB" x1="0" y1="0" x2="0" y2="1"><stop offset="0" stop-color="var(--blue-top)"/><stop offset="1" stop-color="var(--blue-bottom)"/></linearGradient>
        <linearGradient id="orangeB" x1="0" y1="0" x2="0" y2="1"><stop offset="0" stop-color="var(--orange-top)"/><stop offset="1" stop-color="var(--orange-bottom)"/></linearGradient>
      </defs>
      <path d="M0,168 Q70,150 135,185 L135,370 Q70,395 0,355 Z" fill="url(#blueB)"/>
      <path d="M0,360 Q70,400 135,377 L135,508 L0,508 Z" fill="url(#orangeB)"/>
    </svg>
    <div class="layer brand">ZEN<br>TORA</div>
    <div class="layer call"><span class="label">CALL:</span>470-555-0193</div>
    <div class="layer headline">WE PAY<br>CASH FOR<br>HOUSES<br>IN ANY<br>CONDITION!</div>
    <div class="layer services">Probate,<br>Foreclosure,<br>Pass Due<br>Property Taxes,<br>and more!</div>
  </section>

  <section class="banner leader" aria-label="728 by 90 banner">
    <svg class="shapes" viewBox="0 0 657 81" preserveAspectRatio="none" aria-hidden="true">
      <defs>
        <linearGradient id="blueC" x1="0" y1="0" x2="0" y2="1"><stop offset="0" stop-color="var(--blue-top)"/><stop offset="1" stop-color="var(--blue-bottom)"/></linearGradient>
        <linearGradient id="orangeC" x1="0" y1="0" x2="0" y2="1"><stop offset="0" stop-color="var(--orange-top)"/><stop offset="1" stop-color="var(--orange-bottom)"/></linearGradient>
      </defs>
      <path d="M262,0 L472,0 Q462,50 452,81 L242,81 Q245,30 262,0 Z" fill="url(#blueC)"/>
      <path d="M478,0 L657,0 L657,81 L460,81 Q474,50 478,0 Z" fill="url(#orangeC)"/>
    </svg>
    <div class="layer brand">ZENTORA</div>
    <div class="layer call"><span class="label">CALL:</span> 470-555-0193</div>
    <div class="layer headline">WE PAY CASH<br>FOR HOUSES IN<br>ANY CONDITION!</div>
    <div class="layer services">Probate, Foreclosure,<br>Pass Due Property<br>Taxes, and more!</div>
  </section>

  <section class="banner mobile" aria-label="320 by 50 banner">
    <svg class="shapes" viewBox="0 0 490 76" preserveAspectRatio="none" aria-hidden="true">
      <defs>
        <linearGradient id="blueD" x1="0" y1="0" x2="0" y2="1"><stop offset="0" stop-color="var(--blue-top)"/><stop offset="1" stop-color="var(--blue-bottom)"/></linearGradient>
        <linearGradient id="orangeD" x1="0" y1="0" x2="0" y2="1"><stop offset="0" stop-color="var(--orange-top)"/><stop offset="1" stop-color="var(--orange-bottom)"/></linearGradient>
      </defs>
      <path d="M196,0 L352,0 Q344,45 334,76 L178,76 Q180,28 196,0 Z" fill="url(#blueD)"/>
      <path d="M358,0 L490,0 L490,76 L340,76 Q354,45 358,0 Z" fill="url(#orangeD)"/>
    </svg>
    <div class="layer brand">ZENTORA</div>
    <div class="layer call"><span class="label">CALL:</span> 470-555-0193</div>
    <div class="layer headline">WE PAY CASH<br>FOR HOUSES IN<br>ANY CONDITION!</div>
    <div class="layer services">Probate, Foreclosure,<br>Pass Due Property<br>Taxes, and more!</div>
  </section>

  <section class="banner tile" aria-label="100 by 50 banner">
    <svg class="shapes" viewBox="0 0 107 54" preserveAspectRatio="none" aria-hidden="true">
      <defs>
        <linearGradient id="blueE" x1="0" y1="0" x2="0" y2="1"><stop offset="0" stop-color="var(--blue-top)"/><stop offset="1" stop-color="var(--blue-bottom)"/></linearGradient>
        <linearGradient id="orangeE" x1="0" y1="0" x2="0" y2="1"><stop offset="0" stop-color="var(--orange-top)"/><stop offset="1" stop-color="var(--orange-bottom)"/></linearGradient>
      </defs>
      <rect x="0" y="28" width="53" height="26" fill="url(#blueE)"/>
      <rect x="53" y="28" width="54" height="26" fill="url(#orangeE)"/>
    </svg>
    <div class="layer brand">ZENTORA</div>
    <div class="layer call"><span class="label">CALL:</span> 470-555-0193</div>
    <div class="layer headline">WE PAY CASH<br>FOR HOUSES IN<br>ANY CONDITION!</div>
    <div class="layer services">Probate, Foreclosure,<br>Pass Due Property<br>Taxes, and more!</div>
  </section>

</main>
</body>
</html>
```